Illustrationen für Weihnachtstasse
Zielgruppe
Die Varolex GmbH unterstützt Unternehmen und Behörden seit vielen Jahren in den Bereichen DocuHarbor, Consulting sowie Client- und Server-Management.
Aufgabenstellung
Wir als Unternehmen (www.varolex-muster.de) lassen jedes Jahr zu Weihnachten eine Weihnachtstasse mit einer Illustration eines Künstlers/Grafikers für unsere Kunden drucken. Die Auflage ist limitiert und soll eine Besonderheit darstellen.
Wichtig ist:
- es muss ein Weihnachtsmotiv sein (nicht zu verspielt)
- bitte mit Kürzel des Künstlers/Grafikers
- Druckgröße 190x75 mm, 300 dpi
- an der rechten Seite muss noch das Firmen-Logo platziert werden (sollte auf weiß stehen)
- Farben: freie Auswahl – nicht zu bunt

```html
<!DOCTYPE html>
<html lang="de">
<head>
<meta charset="utf-8">
<title>Make Christmas Great Again – Weihnachtstasse Varolex</title>
<link rel="stylesheet" href="https://fonts.googleapis.com/css2?family=Oswald:wght@400;700&display=swap">
<style>
  :root {
    --night: #0c2740;
    --teal: #16607e;
    --cyan: #2fe3f0;
    --orange: #ff5a14;
    --magenta: #b0249a;
    --violet: #6a2bbd;
    --red: #e8283a;
    --cream: #f3d7a8;
    --white: #ffffff;
    --logo-blue: #1f4e79;
  }
  * { margin: 0; padding: 0; box-sizing: border-box; }
  html, body { width: 1200px; height: 475px; overflow: hidden; background: var(--white); }

  .mug-wrap {
    position: relative;
    width: 1200px;
    height: 475px;
    overflow: hidden;
    background:
      radial-gradient(ellipse 520px 360px at 620px 230px, rgba(47,227,240,0.35), transparent 70%),
      linear-gradient(100deg, var(--night) 0%, var(--teal) 38%, #1b7f95 50%, var(--violet) 66%, var(--magenta) 80%, var(--red) 100%);
  }

  .santa-art {
    position: absolute;
    left: 645px;
    top: 0;
    width: 470px;
    height: 475px;
    border-radius: 48% 52% 18% 22% / 30% 34% 10% 10%;
    background:
      radial-gradient(ellipse 170px 150px at 50% 42%, #e7793e, transparent 75%),
      radial-gradient(ellipse 220px 170px at 48% 78%, var(--cream), transparent 72%),
      linear-gradient(180deg, #c8203a 0%, #e53a4a 22%, #f0c89a 40%, #d86a3a 55%, #e8d2b4 80%, #f5e6cf 100%);
  }

  .headline {
    position: absolute;
    left: 135px;
    top: 38px;
    font-family: "Oswald", sans-serif;
    font-weight: 700;
    font-size: 98px;
    line-height: 82px;
    letter-spacing: -1px;
    color: var(--orange);
    text-transform: none;
  }
  .headline .line { display: block; }
  .headline .accent { color: var(--cyan); }

  .logo-plate {
    position: absolute;
    right: 0;
    bottom: 0;
    width: 124px;
    height: 60px;
    background: var(--white);
    border-top-left-radius: 18px;
    display: flex;
    align-items: center;
    justify-content: center;
  }
  .logo-name {
    font-family: "Oswald", sans-serif;
    font-weight: 400;
    font-size: 22px;
    color: var(--logo-blue);
  }
</style>
</head>
<body>
  <div class="mug-wrap">
    <div class="santa-art" role="img" aria-label="Illustration: grimmig rufender Weihnachtsmann mit roter Mütze und weißem Bart im polygonalen Pop-Art-Stil"></div>

    <h1 class="headline">
      <span class="line">mAKE.</span>
      <span class="line">cH<span class="accent">RISTMAS.</span></span>
      <span class="line">GREAT.</span>
      <span class="line">AGAIN.</span>
    </h1>

    <div class="logo-plate">
      <span class="logo-name">Varolex</span>
    </div>
  </div>
</body>
</html>
```